R.T. Halvorsen Electric Holiday Party Invitation

We need a cohesive, on-brand holiday party invitation suite for R.T. Halvorsen Electrical Contractors (slogan Powered Past Limits). Design should include: 1) 5x7" invitation (print + digital), 2) matching RSVP card, and 3) raffle ticket.
Use our brand colors (navy, red, white, light gray) and modern professional style with subtle holiday accents.
Event: Thursday, Dec 18 2025 | 6-10 PM | Brambleton Hall, 418 Larkspur Ave, Hammonton NJ 08094.
RSVP by: Dec 1 | Plus one allowed.
Deliver print-ready PDFs + editable source files.

```html
<!DOCTYPE html>
<html lang="en">
<head>
<meta charset="utf-8">
<title>R.T. Halvorsen Electric – Holiday Party Suite</title>
<link href="https://fonts.googleapis.com/css2?family=Noto+Serif:ital,wght@0,400;0,600;0,700;1,400&display=swap" rel="stylesheet">
<style>
  :root {
    --navy: #2e3a5a;
    --red: #e8343a;
    --white: #ffffff;
    --paper: #ffffff;
  }
  * { margin: 0; padding: 0; box-sizing: border-box; }
  html, body { width: 1200px; height: 922px; overflow: hidden; background: var(--paper); }
  body { position: relative; font-family: "Noto Serif", Georgia, serif; color: var(--navy); }

  .brand {
    position: absolute; display: flex; align-items: center; gap: 6px;
    transform: translateX(-50%); white-space: nowrap;
    font-weight: 700; color: var(--navy); letter-spacing: 0.04em; text-transform: uppercase;
  }
  .brand-dot { width: 10px; height: 10px; border-radius: 50%; background: var(--red); flex: none; }

  .hills { position: absolute; display: block; }
  .hills path { fill: var(--navy); }

  /* Invitation */
  .invitation { position: absolute; left: 151px; top: 138px; width: 459px; height: 642px; background: var(--navy); }
  .invitation-inner { position: absolute; inset: 13px; background: var(--white); overflow: hidden; }
  .invitation .brand { left: 216px; top: 60px; font-size: 17px; }
  .invitation-title {
    position: absolute; left: 0; right: 0; top: 168px; text-align: center;
    font-size: 23px; font-weight: 600; line-height: 1.3;
  }
  .event-date { position: absolute; left: 0; top: 299px; width: 100%; height: 87px; font-size: 14px; font-weight: 600; }
  .event-date span { position: absolute; transform: translate(-50%, -50%); white-space: nowrap; }
  .event-date .rule { position: absolute; top: 0; width: 1.5px; height: 87px; background: var(--navy); }
  .event-venue {
    position: absolute; left: 0; right: 0; top: 397px; text-align: center;
    font-size: 14px; font-weight: 600; line-height: 33px;
  }
  .invitation .hills { left: 11px; top: 405px; }
  .slogan {
    position: absolute; left: 0; right: 0; top: 570px; text-align: center;
    color: var(--white); font-size: 13px;
  }

  /* RSVP card */
  .rsvp { position: absolute; left: 655px; top: 138px; width: 458px; height: 320px; background: var(--navy); }
  .rsvp-inner { position: absolute; left: 15px; top: 15px; right: 15px; bottom: 15px; background: var(--white); overflow: hidden; }
  .rsvp .brand { left: 96px; top: 48px; font-size: 14px; }
  .rsvp-heading {
    position: absolute; right: 52px; top: 38px; font-size: 38px; font-weight: 600; line-height: 1;
  }
  .rsvp-deadline { position: absolute; right: 37px; top: 80px; font-size: 12px; font-style: italic; }
  .rsvp-name { position: absolute; left: 107px; top: 127px; font-size: 13px; font-weight: 600; }
  .rsvp-name-line { position: absolute; left: 158px; top: 142px; width: 192px; height: 1.5px; background: var(--navy); }
  .rsvp-option { position: absolute; font-size: 11px; font-weight: 600; display: flex; align-items: center; gap: 6px; }
  .rsvp-option::before { content: ""; width: 8px; height: 8px; border-radius: 50%; background: var(--navy); }
  .rsvp .hills { left: 0; top: 186px; }

  /* Raffle ticket */
  .ticket { position: absolute; left: 634px; top: 551px; width: 505px; height: 183px; background: var(--navy); }
  .ticket-stub { position: absolute; left: 8px; top: 8px; width: 175px; height: 167px; background: var(--white); }
  .ticket-main { position: absolute; left: 185px; top: 8px; width: 312px; height: 160px; background: var(--white); overflow: hidden; }
  .ticket-stub .brand { left: 88px; top: 20px; font-size: 10px; }
  .ticket-main .brand { left: 55px; top: 20px; font-size: 10px; }
  .stub-field {
    position: absolute; left: 13px; width: 147px; font-size: 12px; font-weight: 600;
    border-bottom: 1.5px solid var(--navy); padding-bottom: 2px;
  }
  .ticket-heading { position: absolute; left: 118px; top: 46px; font-size: 38px; font-weight: 600; line-height: 1; }
  .ticket-details {
    position: absolute; left: 100px; width: 190px; top: 101px; text-align: center;
    font-size: 9.5px; font-weight: 700; line-height: 1.35;
  }
  .ticket-details .date { margin-bottom: 6px; }
  .ticket .hills { left: 0; top: 0; }
</style>
</head>
<body>

<section class="invitation" aria-label="Holiday party invitation">
  <div class="invitation-inner">
    <div class="brand"><span class="brand-dot"></span>R.T. Halvorsen Electric</div>
    <h1 class="invitation-title">HOLIDAY PARTY<br>INVITATION</h1>
    <div class="event-date">
      <span style="left:96px;top:43px">THURSDAY</span>
      <div class="rule" style="left:169px"></div>
      <span style="left:227px;top:14px">DECEMBER</span>
      <span style="left:227px;top:43px">18</span>
      <span style="left:227px;top:73px">2025</span>
      <div class="rule" style="left:275px"></div>
      <span style="left:328px;top:43px">6-10 PM</span>
    </div>
    <svg class="hills" width="411" height="194" viewBox="0 0 411 194" role="img" aria-label="Winter hillside with pine trees and a red cabin">
      <path d="M0,25 C90,20 150,110 230,114 C300,117 340,95 411,95 L411,194 L0,194 Z"/>
    </svg>
    <p class="event-venue">Brambleton Hall, 418 Larkspur Ave,<br>Hammonton NJ 08094</p>
    <p class="slogan">Powered Past Limits</p>
  </div>
</section>

<section class="rsvp" aria-label="RSVP card">
  <div class="rsvp-inner">
    <div class="brand"><span class="brand-dot"></span>R.T. Halvorsen</div>
    <h2 class="rsvp-heading">RSVP</h2>
    <p class="rsvp-deadline">Kindly response by Dec 1 2025</p>
    <p class="rsvp-name">Name :</p>
    <div class="rsvp-name-line"></div>
    <p class="rsvp-option" style="left:133px;top:153px">Attending</p>
    <p class="rsvp-option" style="left:240px;top:153px">Not Attending</p>
    <p class="rsvp-option" style="left:185px;top:190px">Plus one</p>
    <svg class="hills" width="428" height="104" viewBox="0 0 428 104" role="img" aria-label="Winter hillside with pine trees and a red cabin">
      <path d="M0,14 C80,8 150,82 235,90 C305,96 350,72 428,72 L428,104 L0,104 Z"/>
    </svg>
  </div>
</section>

<section class="ticket" aria-label="Raffle ticket">
  <div class="ticket-stub">
    <div class="brand"><span class="brand-dot"></span>R.T. Halvorsen</div>
    <p class="stub-field" style="top:57px">NAME</p>
    <p class="stub-field" style="top:88px">PHONE</p>
    <p class="stub-field" style="top:119px">DATE</p>
  </div>
  <div class="ticket-main">
    <svg class="hills" width="312" height="160" viewBox="0 0 312 160" role="img" aria-label="Winter hillside with pine trees and a red cabin">
      <path d="M0,94 C50,90 90,148 150,156 C210,163 262,140 312,138 L312,160 L0,160 Z"/>
    </svg>
    <div class="brand"><span class="brand-dot"></span>R.T. Halvorsen</div>
    <h2 class="ticket-heading">EVENT</h2>
    <div class="ticket-details">
      <p class="date">Thursday | Dec 18 2025</p>
      <p>Brambleton Hall, 418 Larkspur Ave,<br>Hammonton NJ 08094</p>
    </div>
  </div>
</section>

</body>
</html>
```